In need of a fabulous a newsletter template!

We would like a Newsletter template designed for our practice that we can use on a quarterly basis to send out to our patients via email. This template should also be printable so we may have it printed for our waiting area and use for mailings. We envision a single page, double-sided. We would like to be able to fill out the template with out own material, but have a consistent layout with the following sections: 1) Patient Spotlight, 2) Upcoming Events, 3) Technology Update, 4) Pediatric Corner, 5) Exciting news, 6) Learn to Listen, 7) A note from Dr. Fenwick. To view more about our company, visit our website at www.orchardvalehearing.example

Target Market(s)

Our patients --- Adults age 35-90

Industry/Entity Type

Healthcare

Font styles to use
Serif
Sans Serif

Colors
0892cd
34a7d8
0355a3
3377b5
85cae6

Requirements
Must have
• Eye-catching, organized, easy-to-follow layout so that we may send out information to our patients on a quarterly basis. Once created, we need to be able to fill in the information for the sections listed above. Must list our address and contact information on the front and back; probably in the header on the front and footer on the back.
Nice to have
• Sections 1-5 are needed from above, but would like to fit in sections 6-7, if available.

```html
<!DOCTYPE html>
<html lang="en">
<head>
<meta charset="utf-8">
<title>Orchard Vale Hearing – Quarterly Newsletter</title>
<link href="https://fonts.googleapis.com/css2?family=Jost:wght@400;500;700&display=swap" rel="stylesheet">
<style>
:root{
  --teal:#2bb3c9;
  --teal-dark:#1e9bb2;
  --ink:#4b4b4d;
  --soft:#ebebee;
  --stage:#d9dadd;
  --white:#ffffff;
}
*{box-sizing:border-box;margin:0;padding:0}
html,body{width:1200px;height:857px;overflow:hidden}
body{background:var(--stage);font-family:'Jost',sans-serif;color:var(--ink);position:relative}
.page{position:absolute;top:108px;width:495px;height:640px;background:var(--white);overflow:hidden}
.page--front{left:87px}
.page--back{left:630px}
.abs{position:absolute}
.body-copy{font-size:8.4px;line-height:1.3}
.heading{color:var(--teal);font-weight:700;text-transform:uppercase;font-size:16.5px;line-height:1.05;letter-spacing:.2px}
.photo{position:absolute}

/* brand */
.brand{display:flex;align-items:center;gap:8px;white-space:nowrap}
.brand__dot{width:26px;height:26px;border-radius:50%;background:var(--teal);flex:0 0 auto}
.brand__name{font-size:15px;font-weight:400;color:var(--teal);letter-spacing:.6px;text-transform:uppercase}
.brand--compact{gap:6px}
.brand--compact .brand__dot{width:20px;height:20px}
.brand--compact .brand__name{font-size:12.5px;letter-spacing:.4px}

/* front header */
.masthead__brand{left:34px;top:32px}
.masthead__contact{left:345px;top:35px;font-size:9px;line-height:1.2}
.contact-line{display:flex;align-items:center;gap:4px}
.contact-line svg{width:8px;height:8px}

.hero{left:0;top:89px;width:495px;height:129px;background:linear-gradient(90deg,#e9c5ac 0%,#d8ad91 45%,#3a3a3c 60%,#e6d3c6 75%,#f1e4da 100%)}
.mission{left:0;top:218px;width:495px;height:63px;background:var(--teal);color:var(--white);text-align:center;padding-top:11px}
.mission__title{font-size:17px;font-weight:700;text-transform:uppercase;line-height:1}
.mission__text{font-size:8.4px;line-height:1.25;width:420px;margin:3px auto 0}

.col-left{left:27px;width:210px}
.events{left:270px;top:315px;width:200px}
.event{display:flex;gap:10px;margin-top:10px}
.event svg{flex:0 0 28px;height:28px;margin-top:2px}
.event p{font-size:8.4px;line-height:1.3;width:155px}
.events .event:first-of-type{margin-top:14px}

.anatomy{left:0;top:513px;width:233px;height:123px;background:linear-gradient(120deg,#f3f3f3 0%,#e8c8a8 40%,#d94a3a 60%,#f0d060 80%,#eeeeee 100%)}
.news-panel{left:242px;top:533px;width:253px;height:103px;background:var(--soft)}
.news-tag{left:258px;top:516px;width:128px;height:34px;background:var(--teal);color:var(--white);font-size:16px;font-weight:700;padding:6px 0 0 9px}
.news-tag::after{content:"";position:absolute;left:100px;top:34px;border-left:28px solid transparent;border-top:9px solid var(--teal-dark)}
.news-text{left:258px;top:564px;width:225px;color:#5a5a5c}
.url-tab{left:358px;top:622px;width:117px;height:14px;background:var(--teal);color:var(--white);font-size:7.5px;text-align:center;line-height:14px}
.front-base{left:0;top:636px;width:495px;height:4px;background:var(--teal)}

/* back */
.child-photo{left:0;top:0;width:223px;height:225px;background:linear-gradient(160deg,#9db46a 0%,#c9a38a 35%,#f0cdb9 50%,#8a2f8c 75%,#6b7a45 100%)}
.pediatric{left:239px;top:24px;width:225px}
.pediatric .lead{font-size:8.6px;margin-top:2px}
.pediatric .body-copy{margin-top:13px}

.spotlight{left:0;top:225px;width:495px;height:172px;background:linear-gradient(90deg,var(--teal) 0%,var(--teal) 62%,#7bbf9b 78%,#8aa55a 100%)}
.spotlight__scene{left:340px;top:225px;width:155px;height:172px;background:linear-gradient(100deg,rgba(43,179,201,.9) 0%,#6e9c52 35%,#c9a36b 65%,#b63a4a 100%)}
.spotlight__title{left:20px;top:242px;font-size:16.5px;font-weight:700;color:var(--white);text-transform:uppercase}
.spotlight__avatar{left:19px;top:276px;width:66px;height:66px;border-radius:50%;border:2px solid var(--white);background:linear-gradient(160deg,#5a3a2a,#e9c2a6 60%,#6a98b0)}
.spotlight__quote{left:99px;top:280px;width:180px;color:var(--white)}
.spotlight__quote .sign{margin-top:9px}

.listen{left:0;top:397px;width:495px;height:104px;background:var(--white)}
.listen__title{left:32px;top:421px;font-size:17px;line-height:1.07}
.listen__text{left:104px;top:421px;width:218px}
.device{left:338px;top:397px;width:157px;height:104px;background:linear-gradient(90deg,#ffffff 0%,#e6dbcf 30%,#c9b7a3 55%,#e2d7ca 80%,#ffffff 100%)}

.note{left:0;top:501px;width:495px;height:103px;background:var(--soft)}
.note__brand{left:28px;top:543px}
.note__title{left:244px;top:512px;font-size:16px;font-weight:700;color:var(--teal)}
.note__text{left:244px;top:533px;width:220px}

.footer{left:0;top:604px;width:495px;height:36px;background:linear-gradient(90deg,var(--teal) 0%,#2a9db0 100%);color:var(--white);font-size:7.6px;display:flex;align-items:center;gap:9px;padding-left:26px;white-space:nowrap}
.footer strong{font-weight:700}
.footer span{display:flex;align-items:center;gap:3px}
.footer svg{width:7px;height:7px}
</style>
</head>
<body>

<section class="page page--front">
  <div class="abs brand masthead__brand"><span class="brand__dot"></span><span class="brand__name">Orchard Vale Hearing</span></div>
  <div class="abs masthead__contact">
    <div>412 Alder Bend Rd., Suite 210</div>
    <div>Millbrook, SC 29900</div>
    <div class="contact-line"><svg viewBox="0 0 10 10"><path d="M2 1 L4 1 L4.5 3 L3.3 3.8 Q4.3 6 6.2 6.7 L7 5.5 L9 6 L9 8 Q5 9 2 5 Q1 3 2 1Z" fill="#2bb3c9"/></svg>(555) 014-2280</div>
    <div class="contact-line"><svg viewBox="0 0 10 10"><rect x="1" y="4" width="8" height="4" fill="#2bb3c9"/><rect x="3" y="1" width="4" height="3" fill="none" stroke="#2bb3c9"/><rect x="3" y="6" width="4" height="3" fill="#fff" stroke="#2bb3c9"/></svg>(555) 014-2291</div>
  </div>

  <div class="photo hero" role="img" aria-label="Photo of an audiologist examining a man's ear with an otoscope"></div>

  <div class="abs mission">
    <h1 class="mission__title">Hearing Care for All Ages</h1>
    <p class="mission__text">Orchard Vale Hearing exists to provide exceptional hearing healthcare for patients of all ages. Our goal is to successfully bridge the gap between diagnosis and treatment for those with hearing loss.</p>
  </div>

  <div class="abs col-left" style="top:306px">
    <h2 class="heading">Exceptional<br>Hearing Healthcare</h2>
    <p class="body-copy" style="margin-top:2px">At Orchard Vale Hearing, you can expect your patient experience to be met with easy communication, prompt follow-up, and the highest level of diagnostics, hearing device selection, fitting and maintenance.</p>
  </div>

  <div class="abs col-left" style="top:414px">
    <h2 class="heading">Technology Update</h2>
    <p class="body-copy" style="margin-top:4px">Lorem ipsum dolor sit amet, consectetur adipiscing elit, sed do eiusmod tempor incididunt ut labore et dolore magna aliqua. Ut enim ad minim veniam, quis nostrud exercitation ullamco laboris nisi ut aliquip ex ea commodo consequat. Duis aute irure dolor in reprehenderit in voluptate velit esse cillum dolore eu fugiat nulla pariatur.</p>
  </div>

  <div class="abs events">
    <h2 class="heading">Upcoming Events</h2>
    <div class="event">
      <svg viewBox="0 0 28 28"><rect x="1" y="4" width="26" height="23" rx="2" fill="none" stroke="#3a3a3c" stroke-width="2"/><rect x="1" y="4" width="26" height="6" fill="#3a3a3c"/><rect x="7" y="1" width="2" height="6" fill="#3a3a3c"/><rect x="19" y="1" width="2" height="6" fill="#3a3a3c"/><g fill="#2bb3c9"><rect x="5" y="13" width="4" height="3"/><rect x="10.5" y="13" width="4" height="3"/><rect x="16" y="13" width="4" height="3"/><rect x="21" y="13" width="3" height="3"/><rect x="5" y="18" width="4" height="3"/><rect x="10.5" y="18" width="4" height="3"/><rect x="16" y="18" width="4" height="3"/><rect x="21" y="18" width="3" height="3"/></g></svg>
      <p>Lorem ipsum dolor sit amet, consectetur adipiscing elit, sed do eiusmod tempor incididunt ut labore et dolore magna aliqua.</p>
    </div>
    <div class="event">
      <svg viewBox="0 0 28 28"><rect x="1" y="4" width="26" height="23" rx="2" fill="none" stroke="#3a3a3c" stroke-width="2"/><rect x="1" y="4" width="26" height="6" fill="#3a3a3c"/><rect x="7" y="1" width="2" height="6" fill="#3a3a3c"/><rect x="19" y="1" width="2" height="6" fill="#3a3a3c"/><g fill="#2bb3c9"><rect x="5" y="13" width="4" height="3"/><rect x="10.5" y="13" width="4" height="3"/><rect x="16" y="13" width="4" height="3"/><rect x="21" y="13" width="3" height="3"/><rect x="5" y="18" width="4" height="3"/><rect x="10.5" y="18" width="4" height="3"/><rect x="16" y="18" width="4" height="3"/><rect x="21" y="18" width="3" height="3"/></g></svg>
      <p>Lorem ipsum dolor sit amet, consectetur adipiscing elit, sed do eiusmod tempor incididunt ut labore et dolore magna aliqua.</p>
    </div>
    <div class="event">
      <svg viewBox="0 0 28 28"><rect x="1" y="4" width="26" height="23" rx="2" fill="none" stroke="#3a3a3c" stroke-width="2"/><rect x="1" y="4" width="26" height="6" fill="#3a3a3c"/><rect x="7" y="1" width="2" height="6" fill="#3a3a3c"/><rect x="19" y="1" width="2" height="6" fill="#3a3a3c"/><g fill="#2bb3c9"><rect x="5" y="13" width="4" height="3"/><rect x="10.5" y="13" width="4" height="3"/><rect x="16" y="13" width="4" height="3"/><rect x="21" y="13" width="3" height="3"/><rect x="5" y="18" width="4" height="3"/><rect x="10.5" y="18" width="4" height="3"/><rect x="16" y="18" width="4" height="3"/><rect x="21" y="18" width="3" height="3"/></g></svg>
      <p>Lorem ipsum dolor sit amet, consectetur adipiscing elit, sed do eiusmod tempor incididunt ut labore et dolore magna aliqua.</p>
    </div>
  </div>

  <div class="photo anatomy" role="img" aria-label="Photo of a hand pointing at a colourful anatomical ear model"></div>
  <div class="abs news-panel"></div>
  <div class="abs news-tag">Exciting news</div>
  <p class="abs body-copy news-text">Lorem ipsum dolor sit amet, consectetur adipiscing elit, sed do eiusmod tempor incididunt ut labore et dolore magna aliqua. Ut enim ad minim veniam, quis nostrud exercitation ullamco laboris nisi ut aliquip ex ea commodo consequat.</p>
  <div class="abs url-tab">www.orchardvalehearing.example</div>
  <div class="abs front-base"></div>
</section>

<section class="page page--back">
  <div class="photo child-photo" role="img" aria-label="Photo of a smiling toddler wearing a flower headband and a hearing aid"></div>
  <div class="abs pediatric">
    <h2 class="heading">Pediatric Corner</h2>
    <p class="lead">Our goal is to maximize every child's hearing potential.</p>
    <p class="body-copy">The Pediatric Audiology Program at Orchard Vale Hearing provides comprehensive testing, treatment and support services for children of all ages and their families. Our Doctors of Audiology are the only audiologists in the area specialize in Pediatric Audiology, as recognized by the Northland Board of Audiology. With over 20 years combined experience, Drs. Fenwick and Haldane recognize that the pediatric population requires a unique skill set. We are fully equipped to see children of all ages with developmental delays and medical conditions. We offer both behavioral and electroacoustic testing to ensure a thorough and accurate diagnosis of hearing sensitivity and evaluation of the auditory system.</p>
  </div>

  <div class="abs spotlight"></div>
  <div class="photo spotlight__scene" role="img" aria-label="Photo of a mother and grandmother seated on hay bales at an autumn garden party"></div>
  <h2 class="abs spotlight__title">Patient Spotlight</h2>
  <div class="photo spotlight__avatar" role="img" aria-label="Portrait photo of the quoted patient's mother"></div>
  <div class="abs body-copy spotlight__quote">
    <p>What a great experience my daughter and I had at Orchard Vale Hearing. Dr. Fenwick relates so well not only to the parents but, to the child as well. She thoroughly explained all tests and results. Dr. Fenwick even had a hearing tea party celebration when my daughter received her first hearing device. Top notch service. Thank you.</p>
    <p class="sign">– Maren</p>
  </div>

  <div class="abs listen"></div>
  <h2 class="abs heading listen__title">Learn<br>to<br>Listen</h2>
  <p class="abs body-copy listen__text">Lorem ipsum dolor sit amet, consectetur adipiscing elit, sed do eiusmod tempor incididunt ut labore et dolore magna aliqua. Ut enim ad minim veniam, quis nostrud exercitation ullamco laboris nisi ut aliquip ex ea commodo consequat. Duis aute irure dolor in reprehenderit in voluptate velit esse cillum dolore eu fugiat nulla pariatur.</p>
  <div class="photo device" role="img" aria-label="Product photo of two behind-the-ear hearing aids"></div>

  <div class="abs note"></div>
  <div class="abs brand brand--compact note__brand"><span class="brand__dot"></span><span class="brand__name">Orchard Vale Hearing</span></div>
  <h2 class="abs note__title">A note from Dr.</h2>
  <p class="abs body-copy note__text">Lorem ipsum dolor sit amet, consectetur adipiscing elit, sed do eiusmod tempor incididunt ut labore et dolore magna aliqua. Ut enim ad minim veniam, quis nostrud exercitation ullamco laboris nisi ut aliquip ex ea commodo consequat. Duis aute irure dolor in reprehenderit in voluptate velit esse cillum dolore eu fugiat nulla pariatur.</p>

  <footer class="abs footer">
    <span>412 Alder Bend Rd., Suite 210, Millbrook, SC 29900</span>
    <span><svg viewBox="0 0 10 10"><path d="M2 1 L4 1 L4.5 3 L3.3 3.8 Q4.3 6 6.2 6.7 L7 5.5 L9 6 L9 8 Q5 9 2 5 Q1 3 2 1Z" fill="#fff"/></svg><strong>(555) 014-2280</strong></span>
    <span><svg viewBox="0 0 10 10"><rect x="1" y="4" width="8" height="4" fill="#fff"/><rect x="3" y="1" width="4" height="3" fill="none" stroke="#fff"/></svg><strong>(555) 014-2291</strong></span>
    <span><svg viewBox="0 0 10 10"><circle cx="5" cy="5" r="4" fill="#fff"/></svg>www.orchardvalehearing.example</span>
  </footer>
</section>

</body>
</html>
```